50th Invite

Design a 50th birthday invite.

Key essentials to communicate are:

Date: 14 December 2019
Time: 7pm for 7.30pm departure
Birthday person: Glen
Theme: Boat Party
Location: Berth K4 27, Fernquay

Other than that will leave to your creativity. Just for clarity, the above is info to be communicated somehow on the invite, I dont want it to be simply copied.

i would like a luxury boat theme, think Miami, Bahamas etc etc, photos or drawings OK

```html
<!DOCTYPE html>
<html lang="en">
<head>
<meta charset="utf-8">
<title>50th Birthday Invite – Glen</title>
<link rel="stylesheet" href="https://fonts.googleapis.com/css2?family=Source+Sans+3:wght@200;300;400&display=swap">
<style>
  :root {
    --page-bg: #ffffff;
    --sea-top: #2b3a8e;
    --sea-mid: #0857a6;
    --sea-bottom: #00aeea;
    --hot-pink: #ec0b8c;
    --silver: #a9abae;
    --silver-light: #d6d7d9;
    --text-white: #ffffff;
    --leaf-green: #8cc63f;
    --scene-blue: #0c5aa5;
  }
  * { margin: 0; padding: 0; box-sizing: border-box; }
  html, body {
    width: 1200px;
    height: 1200px;
    overflow: hidden;
    background: var(--page-bg);
  }
  .canvas {
    position: relative;
    width: 1200px;
    height: 1200px;
    background: var(--page-bg);
  }
  .invite {
    position: absolute;
    left: 179px;
    top: 46px;
    width: 807px;
    height: 1072px;
    overflow: hidden;
    background: linear-gradient(to bottom, var(--sea-top) 0%, var(--sea-mid) 22%, #0a79c4 60%, var(--sea-bottom) 100%);
    font-family: "Source Sans 3", "Myriad Pro", sans-serif;
    color: var(--text-white);
  }
  .age-numeral {
    position: absolute;
    left: 62px;
    top: 10px;
    font-size: 470px;
    line-height: 1;
    font-weight: 200;
    color: var(--hot-pink);
  }
  .age-ring {
    position: absolute;
    left: 355px;
    top: 111px;
    width: 336px;
    height: 336px;
  }
  .age-suffix {
    position: absolute;
    left: 655px;
    top: 382px;
    font-size: 54px;
    font-weight: 300;
    color: var(--silver);
    line-height: 1;
  }
  .rule {
    position: absolute;
    height: 3px;
    background: var(--hot-pink);
  }
  .rule--top { left: 104px; top: 459px; width: 606px; }
  .rule--bottom { left: 110px; top: 564px; width: 604px; }
  .headline {
    position: absolute;
    left: 104px;
    top: 482px;
    width: 610px;
    display: flex;
    justify-content: space-between;
    font-size: 76px;
    font-weight: 200;
    line-height: 1;
  }
  .details {
    position: absolute;
    left: 63px;
    top: 646px;
    list-style: none;
    font-size: 39px;
    font-weight: 300;
    letter-spacing: 0.11em;
    line-height: 49px;
  }
  .leaf {
    position: absolute;
  }
  .leaf--top { left: 0; top: 0; width: 302px; height: 143px; }
  .leaf--bottom { right: 0; bottom: 0; width: 300px; height: 158px; }
</style>
</head>
<body>
<main class="canvas">
  <section class="invite">
    <div class="age-numeral">5</div>

    <svg class="age-ring" viewBox="0 0 336 336" aria-hidden="false">
      <defs>
        <linearGradient id="silverRing" x1="0" y1="0" x2="1" y2="1">
          <stop offset="0" stop-color="var(--silver-light)"/>
          <stop offset="0.5" stop-color="var(--silver)"/>
          <stop offset="1" stop-color="var(--silver-light)"/>
        </linearGradient>
      </defs>
      <circle cx="168" cy="168" r="152" fill="var(--scene-blue)" role="img" aria-label="Sailboat and palm tree island above rolling waves"/>
      <circle cx="168" cy="168" r="152" fill="none" stroke="url(#silverRing)" stroke-width="16"/>
    </svg>

    <div class="age-suffix">th</div>

    <div class="rule rule--top"></div>
    <h1 class="headline" aria-label="Birthday">
      <span>B</span><span>I</span><span>R</span><span>T</span><span>H</span><span>D</span><span>A</span><span>Y</span>
    </h1>
    <div class="rule rule--bottom"></div>

    <ul class="details">
      <li>Date: 14 December 2019</li>
      <li>Time: 7pm for 7:30 departure</li>
      <li>Birthday Person:Glen</li>
      <li>Theme: Boat Party</li>
      <li>Location: Berth K4 27, Fernquay</li>
    </ul>

    <svg class="leaf leaf--top" viewBox="0 0 302 143" role="img" aria-label="Tropical palm frond">
      <path d="M0 0 H302 C240 40 160 70 110 143 C60 110 20 80 0 60 Z" fill="var(--leaf-green)" opacity="0.9"/>
    </svg>
    <svg class="leaf leaf--bottom" viewBox="0 0 300 158" role="img" aria-label="Tropical palm frond">
      <path d="M300 0 V158 H0 C60 120 120 60 200 30 C240 15 270 5 300 0 Z" fill="var(--leaf-green)" opacity="0.9"/>
    </svg>
  </section>
</main>
</body>
</html>
```